New furniture company needs a cool, fresh Website - think lounjo.com, velmora.com

Quiltrest.com: We are launching a home (Shopify) furniture business, aimed at the young, discerning mid-market consumer. The aim is to compete with many furniture e-tailers, as well as more established retail brands.
We want the website to capture the hearts, minds and wallets of the target audience, placing Quiltrest.com firmly into the market place. Please look to Velmora.com for look and feel inspiration. We will be selling approx 15 products to start. I suggest using Shopify with the following theme please: – Hearth & Meadow – Cadenza – Ravel. Please see the logo below. The website needs to have a sophisticated feel for affordable aspirational furniture. Soft colours and homely text - please go with look and feel of Velmora.com. Please see a below file containing image of some sofas, chairs and footstools that will be for sale.
Many thanks

Target Market(s)

mid-market, young families looking for cool, affordable, easy to buy furniture

Industry/Entity Type

Furniture

Coding

Coded - Design and coding required

Number of Pages Required

5+ page

Font styles to use
Sans Serif

Colors
86cae7
cee9f5
3277b5
eaf2ce
fdf9ce
fff3d1
0255a3
e8e8e8
cbcbcb

Requirements
Must have
• Shopify
• http://www.velmora.com/hartwick-leather-large-sofa.html - great example of what we need it to look like
• logo as shown
• homepage
• products menu - sofas, seating, footstools, antique
• images of all products (examples provided) with ability to click on various fabric swatch samples and see the sofa in different fabrics and colours (check out lounjo.com)
• facility for social media
• facility to buy online
• "add to wishlist"
• "add to basket"
Nice to have
• I want it to have a light and airy feel, nothing too heavy or corporate. Needs to be very easily navigated and a simple approach
Should not have
• Dark, heavy colours

```html
<!DOCTYPE html>
<html lang="en">
<head>
<meta charset="utf-8">
<title>Quiltrest — Home</title>
<link href="https://fonts.googleapis.com/css2?family=Lato:wght@300;400;700;900&family=Open+Sans:wght@400;600&display=swap" rel="stylesheet">
<style>
:root{
  --blue:#2f7ab9;
  --blue-deep:#0255a3;
  --ink:#3a3a3a;
  --muted:#8a8a8a;
  --line:#dcdcdc;
  --panel:#e8e8e8;
  --panel-soft:#f1f1f1;
  --nav:#5e5e5e;
  --banner:#7b7b7b;
  --footer:#1f1f1f;
  --footer-bottom:#161616;
  --white:#ffffff;
}
*{box-sizing:border-box;margin:0;padding:0}
html,body{width:1200px;height:2924px;overflow:hidden;background:var(--white)}
body{font-family:"Open Sans",Arial,sans-serif;color:var(--ink);position:relative}
.section{position:absolute;left:0;width:1200px}
.wrap{position:absolute;left:88px;width:1024px}
h1,h2,h3,h4,.display{font-family:"Lato",Arial,sans-serif}

/* top bar */
.topbar{top:0;height:48px;border-bottom:1px solid var(--line);font-size:12px;color:var(--muted)}
.topbar .wrap{top:0;height:48px;display:flex;align-items:center;gap:28px;letter-spacing:.5px}
.topbar b{color:var(--ink);font-weight:600}

/* header */
.header{top:48px;height:102px}
.header .wrap{top:0;height:102px;display:flex;align-items:center;justify-content:space-between}
.header-links{display:flex;gap:24px;font-size:12px;letter-spacing:1px;color:var(--ink);width:300px}
.brand{display:flex;flex-direction:column;align-items:center;gap:6px}
.brand-mark{width:26px;height:26px;border:2px solid var(--ink);border-radius:50%}
.brand-name{font-family:"Lato",sans-serif;font-weight:700;font-size:22px;letter-spacing:5px;color:var(--ink)}
.search{width:300px;display:flex;justify-content:flex-end}
.search-box{width:250px;height:34px;border:1px solid var(--line);display:flex;align-items:center;justify-content:space-between;padding:0 12px;font-size:12px;color:var(--muted)}

/* nav */
.mainnav{top:150px;height:36px;background:var(--nav)}
.mainnav .wrap{top:0;height:36px;display:flex;align-items:center;gap:30px;font-size:13px;color:var(--white)}
.mainnav .cart{margin-left:auto}

/* hero */
.hero{top:212px;left:88px;width:1024px;height:428px;background:var(--panel)}
.hero-img{position:absolute;left:30px;top:44px;width:470px;height:320px;background:linear-gradient(160deg,#5a2e44,#3d1d2e 70%,#c9c3c0 70%);border-radius:2px}
.hero-text{position:absolute;left:536px;top:30px;width:460px}
.hero-text h2{font-weight:300;font-size:36px;color:var(--blue);letter-spacing:1px;line-height:1.1}
.hero-text h2 strong{font-weight:900;display:block}
.hero-text p{margin-top:14px;font-size:12px;line-height:1.55;color:var(--muted)}
.hero-price{margin-top:18px;font-family:"Lato",sans-serif;font-weight:900;font-size:34px;color:var(--ink)}
.btn{display:inline-block;border:1px solid #b5b5b5;border-radius:2px;padding:8px 16px;font-size:11px;letter-spacing:1px;color:var(--ink);background:var(--white)}
.hero-text .btn{margin-top:22px}
.swatches{display:flex;gap:14px;margin-top:30px}
.swatch{width:62px;height:46px;background:var(--white);border:1px solid var(--line);display:flex;align-items:center;justify-content:center}
.swatch i{display:block;width:44px;height:22px;background:#4a2538;border-radius:3px}

/* products */
.products{top:664px;left:88px;width:1024px;height:396px;display:flex;gap:12px}
.card{flex:1;border:1px solid var(--line);text-align:center;padding:18px 14px}
.card-img{height:200px;border-radius:2px}
.card h4{margin-top:22px;font-weight:400;font-size:13px;color:var(--ink)}
.stars{margin-top:10px;font-size:13px;letter-spacing:3px;color:#c4c4c4}
.card .price{margin-top:10px;font-family:"Lato",sans-serif;font-weight:900;font-size:26px;color:var(--blue)}
.card .btn{margin-top:12px;font-size:10px;padding:6px 12px}

/* promos */
.promo{position:absolute;background:var(--panel)}
.promo-small{left:88px;width:400px;height:284px}
.promo-a{top:1072px}
.promo-b{top:1368px}
.promo-small h3{font-weight:700;font-size:17px;color:var(--nav);letter-spacing:1px}
.promo-small p{margin-top:6px;font-size:11px;line-height:1.5;color:var(--muted)}
.promo-small .price{margin-top:22px;font-family:"Lato",sans-serif;font-weight:900;font-size:26px;color:var(--blue)}
.promo-small .btn{margin-top:18px}
.promo-a .txt{position:absolute;left:26px;top:30px;width:230px}
.promo-a .img{position:absolute;right:22px;top:110px;width:140px;height:170px;background:linear-gradient(#e4d2be,#c8ae94);border-radius:40px 40px 6px 6px}
.promo-b .txt{position:absolute;left:170px;top:26px;width:212px;text-align:right}
.promo-b .img{position:absolute;left:20px;top:90px;width:140px;height:170px;background:linear-gradient(#8a7450,#5f4d33);border-radius:40px 40px 6px 6px}
.promo-large{top:1072px;left:500px;width:612px;height:580px;text-align:center}
.promo-large h3{margin-top:36px;font-weight:700;font-size:24px;letter-spacing:1.5px;color:var(--nav)}
.promo-large p{margin:12px auto 0;width:400px;font-size:11px;line-height:1.5;color:var(--muted)}
.promo-large .img{margin:56px auto 0;width:420px;height:190px;background:linear-gradient(#6d7a2a,#4e5a1a);border-radius:60px 60px 10px 10px}
.promo-large .price{margin-top:26px;font-family:"Lato",sans-serif;font-weight:900;font-size:28px;color:var(--ink)}
.promo-large .btn{margin-top:18px}

/* offer banner */
.offer{top:1672px;left:88px;width:1024px;height:280px}
.offer-box{position:absolute;left:0;top:0;width:352px;height:280px;background:var(--banner);color:var(--white);padding:30px 40px}
.offer-box h3{font-weight:400;font-size:24px;letter-spacing:2px}
.offer-box .big{margin-top:16px;font-family:"Lato",sans-serif;font-weight:900;font-size:96px;line-height:1}
.offer-box .big small{font-size:30px;font-weight:700;margin-left:6px}
.offer-box p{margin-top:18px;font-size:11px;line-height:1.5;color:#e6e6e6}
.offer-box .btn{margin-top:16px;background:transparent;border-color:#e6e6e6;color:var(--white)}
.offer-img{position:absolute;left:360px;top:0;width:664px;height:280px;background:linear-gradient(180deg,#3c3c3c 0%,#606060 45%,#9a9a9a 100%)}

/* blog */
.blog{top:1968px;left:88px;width:1024px;height:480px;display:flex;gap:16px}
.post{flex:1}
.post-img{height:330px}
.post-img.grey{background:linear-gradient(#6b6460,#8d8a86 60%,#b8aea2)}
.post-img.red{background:linear-gradient(#5a4a42,#6f2024 55%,#b8a99a)}
.post .date{margin-top:16px;font-size:12px;color:var(--muted)}
.post h4{margin-top:6px;font-weight:700;font-size:20px;color:var(--ink)}
.post p{margin-top:8px;font-size:11px;line-height:1.5;color:var(--muted)}

/* brands */
.brands{top:2480px;height:128px;background:var(--panel-soft)}
.brands .wrap{top:0;height:128px;display:flex;align-items:center;justify-content:space-around}
.brand-item{font-family:"Lato",sans-serif;font-weight:700;font-size:24px;letter-spacing:2px;color:#a3a3a3}

/* footer */
.footer{top:2608px;height:272px;background:var(--footer);color:#b0b0b0}
.footer .wrap{top:36px;display:flex;gap:40px}
.fcol{width:220px}
.fcol h5{font-family:"Lato",sans-serif;font-weight:700;font-size:12px;letter-spacing:1px;color:var(--white);margin-bottom:12px}
.fcol li{list-style:none;font-size:11px;line-height:22px}
.news{display:flex;margin-top:2px}
.news span{flex:1;height:30px;background:var(--white);font-size:11px;color:var(--muted);padding:8px 10px}
.news b{width:88px;height:30px;background:var(--blue);color:var(--white);font-size:11px;font-weight:600;display:flex;align-items:center;justify-content:center}
.social,.pay{display:flex;gap:8px;margin-top:10px}
.social i{display:block;width:24px;height:24px;background:#3a3a3a}
.pay i{display:block;width:40px;height:24px;background:#d8d8d8;border-radius:2px}
.pay i:nth-child(2){background:#9fb8d8}
.pay i:nth-child(3){background:#e6c9a0}
.pay i:nth-child(4){background:#a9c4e0}
.footer-bottom{top:2880px;height:44px;background:var(--footer-bottom);font-size:11px;color:#8d8d8d;text-align:center;line-height:44px}
</style>
</head>
<body>

<div class="section topbar">
  <div class="wrap"><span>CALL: 0800-555-0142</span><b>GBP ▾</b></div>
</div>

<header class="section header">
  <div class="wrap">
    <nav class="header-links"><span>ABOUT US</span><span>BLOG</span><span>SHOP</span></nav>
    <div class="brand"><span class="brand-mark"></span><span class="brand-name">QUILTREST</span></div>
    <div class="search">
      <div class="search-box"><span>Search</span>
        <svg width="14" height="14" viewBox="0 0 14 14"><circle cx="6" cy="6" r="4.5" fill="none" stroke="#8a8a8a" stroke-width="1.5"/><line x1="9.3" y1="9.3" x2="13" y2="13" stroke="#8a8a8a" stroke-width="1.5"/></svg>
      </div>
    </div>
  </div>
</header>

<nav class="section mainnav">
  <div class="wrap">
    <span>Sofas</span><span>Armchairs</span><span>Beds</span><span>Accessories</span><span>Free samples!</span><span>Showrooms</span><span>Why us?</span><span>Offers</span>
    <svg class="cart" width="18" height="16" viewBox="0 0 18 16"><path d="M1 1h3l2 9h9l2-6H5" fill="none" stroke="#fff" stroke-width="1.5"/><circle cx="7" cy="14" r="1.4" fill="#fff"/><circle cx="14" cy="14" r="1.4" fill="#fff"/></svg>
  </div>
</nav>

<section class="section hero">
  <div class="hero-img" role="img" aria-label="Plum velvet chesterfield sofa"></div>
  <div class="hero-text">
    <h2>PELLENTESQUE PURUS <strong>VESTIBULUM VIVERRA.</strong></h2>
    <p>Nam fermentum arcu at orci mattis tincidunt. Curabitur posuere justo sit amet nibh rutrum tempus. Proin vehicula tristique lectus eget tincidunt. Integer auctor felis vel dolor semper lacus.</p>
    <div class="hero-price">$1,971</div>
    <span class="btn">BUY NOW</span>
    <div class="swatches"><span class="swatch"><i></i></span><span class="swatch"><i></i></span><span class="swatch"><i></i></span></div>
  </div>
</section>

<section class="section products">
  <article class="card"><div class="card-img" role="img" aria-label="Sage green lounge armchair" style="background:linear-gradient(#8f9c84,#6e7d64)"></div><h4>Pellentesque Ornare Mauris</h4><div class="stars">★★★★★</div><div class="price">$250</div><span class="btn">ADD TO CART</span></article>
  <article class="card"><div class="card-img" role="img" aria-label="Cream wingback armchair" style="background:linear-gradient(#ece6dc,#d5cabb)"></div><h4>Pellentesque Ornare Mauris</h4><div class="stars">★★★★★</div><div class="price">$250</div><span class="btn">ADD TO CART</span></article>
  <article class="card"><div class="card-img" role="img" aria-label="Ivory chesterfield sofa" style="background:linear-gradient(#eee9df,#d7cfc1)"></div><h4>Pellentesque Ornare Mauris</h4><div class="stars">★★★★★</div><div class="price">$250</div><span class="btn">ADD TO CART</span></article>
  <article class="card"><div class="card-img" role="img" aria-label="Beige daybed with wooden frame" style="background:linear-gradient(#d9c9ad,#b49c78)"></div><h4>Pellentesque Ornare Mauris</h4><div class="stars">★★★★★</div><div class="price">$250</div><span class="btn">ADD TO CART</span></article>
</section>

<section class="promo promo-small promo-a">
  <div class="txt"><h3>MAECENAS AT NISL MATTIS</h3><p>Lacus vel facilisis volutpat est velit egestas dui id ornare.</p><div class="price">$508</div><span class="btn">BUY NOW</span></div>
  <div class="img" role="img" aria-label="Beige upholstered accent chair"></div>
</section>
<section class="promo promo-small promo-b">
  <div class="txt"><h3>MAECENAS AT NISL MATTIS</h3><p>Lacus vel facilisis volutpat est velit egestas dui id ornare.</p><div class="price">$508</div><span class="btn">BUY NOW</span></div>
  <div class="img" role="img" aria-label="Olive brown fabric armchair"></div>
</section>
<section class="promo promo-large">
  <h3>NULLA FACILISIS1 LAOREET</h3>
  <p>Duis sed mauris ac tortor consequat. Pellentesque vel semper sollicitudin ante, non malesuada augue lorem.</p>
  <div class="img" role="img" aria-label="Olive green velvet sofa"></div>
  <div class="price">$5,999</div>
  <span class="btn">BUY NOW</span>
</section>

<section class="section offer">
  <div class="offer-box">
    <h3>LETEST DESIGN</h3>
    <div class="big">75%<small>OFF</small></div>
    <p>Donec mattis feugiat fringilla. Vivamus in leo nulla, ornare nec.</p>
    <span class="btn">SHOP NOW</span>
  </div>
  <div class="offer-img" role="img" aria-label="Grey sofa in a softly lit living room"></div>
</section>

<section class="section blog">
  <article class="post">
    <div class="post-img grey" role="img" aria-label="Grey fabric sofa against a stone wall"></div>
    <div class="date">◷ Friday, February 03, 2017</div>
    <h4>Pellentesque habitant morbi tr...</h4>
    <p>Fusce at pharetra arcu. Sed nisl lacus, ultrices at iaculis nec, aliquet ut nisi. Nullam volutpat ex ut metus, condimentum est quis dapibus, aenean lorem ipsum.</p>
  </article>
  <article class="post">
    <div class="post-img red" role="img" aria-label="Deep red velvet chesterfield sofa"></div>
    <div class="date">◷ Friday, February 03, 2017</div>
    <h4>Pellentesque habitant morbi tr...</h4>
    <p>Fusce at pharetra arcu. Sed nisl lacus, ultrices at iaculis nec, aliquet ut nisi. Nullam volutpat ex ut metus, condimentum est quis dapibus, aenean lorem ipsum.</p>
  </article>
</section>

<section class="section brands">
  <div class="wrap"><span class="brand-item">BRAND</span><span class="brand-item">BRAND</span><span class="brand-item">BRAND</span><span class="brand-item">BRAND</span><span class="brand-item">BRAND</span><span class="brand-item">BRAND</span></div>
</section>

<footer class="section footer">
  <div class="wrap">
    <div class="fcol"><h5>SHOPPING GUIDE</h5><ul><li>Help</li><li>FAQs</li><li>Payment</li><li>Shipment</li><li>Where is my order?</li><li>Return Policy</li></ul></div>
    <div class="fcol"><h5>STYLE ADVISOR</h5><ul><li>Your Account</li><li>Information</li><li>Addresses</li><li>Discount</li><li>Orders History</li><li>Additional Information</li></ul></div>
    <div class="fcol"><h5>INFORMATION</h5><ul><li>About Us</li><li>Contact Us</li><li>Reviews</li><li>Delivery</li><li>Sitemap</li><li>Suppliers</li><li>Search Terms</li></ul></div>
    <div class="fcol">
      <h5>NEWSLETTER</h5>
      <div class="news"><span>Enter your email</span><b>SUBSCRIBE</b></div>
      <h5 style="margin-top:20px">FOLLOW US</h5>
      <div class="social"><i></i><i></i><i></i><i></i><i></i><i></i></div>
      <div class="pay"><i></i><i></i><i></i><i></i></div>
    </div>
  </div>
</footer>
<div class="section footer-bottom">© 2017 All Rights Reserved Quiltrest.com</div>

</body>
</html>
```